Caldrow Supplies Business Card

Professional business card that stand out to our potential customers. Front and back with clean modern design

Industry/Entity Type

Oil and gas

Contact Information for Business Card

Name, address, website , office phone and cell number

Requirements
Must have
• Editable files for each employee

```html
<!DOCTYPE html>
<html lang="en">
<head>
<meta charset="utf-8">
<title>Caldrow Supplies Business Card</title>
<link rel="stylesheet" href="https://fonts.googleapis.com/css2?family=Arimo:wght@400;700&display=swap">
<style>
  :root {
    --backdrop: #3d3d3d;
    --card-black: #262626;
    --panel-black: #1c1c1c;
    --signal-red: #ff0000;
    --accent-cyan: #1fa8d1;
    --ink-white: #ffffff;
    --mark-grey: #4a4a4a;
    --soft-grey: #5c5c5c;
  }
  * { margin: 0; padding: 0; box-sizing: border-box; }
  html, body {
    width: 1200px; height: 803px; overflow: hidden;
    background: var(--backdrop);
    font-family: "Arimo", Arial, sans-serif;
  }
  .stage {
    width: 1200px; height: 803px;
    display: flex; align-items: center; justify-content: center; gap: 44px;
  }
  .card {
    position: relative;
    width: 525px; height: 300px;
    border-radius: 18px;
    overflow: hidden;
    box-shadow: 0 14px 30px rgba(0,0,0,.35);
  }
  /* Front */
  .card-front { background: var(--signal-red); }
  .front-panel { position: absolute; inset: 0; }
  .front-panel-name {
    position: absolute; left: 30px; bottom: 38px;
    width: 170px;
    font-weight: 700; font-size: 26px; line-height: 1.05;
    letter-spacing: 1px; text-transform: uppercase;
    color: var(--mark-grey);
  }
  .front-content {
    position: absolute; left: 238px; top: 30px; right: 24px;
    color: var(--ink-white);
  }
  .brand-lockup {
    display: flex; align-items: center; gap: 8px;
    font-weight: 700; font-size: 17px; letter-spacing: 1.5px;
    text-transform: uppercase; color: var(--ink-white);
  }
  .brand-square { width: 12px; height: 12px; background: var(--ink-white); }
  .person-name {
    margin-top: 28px;
    font-weight: 700; font-size: 24px; letter-spacing: .5px;
    text-transform: uppercase;
  }
  .person-title { font-size: 12px; margin-top: 2px; }
  .address { margin-top: 18px; font-size: 12.5px; line-height: 1.35; }
  .contact-list { margin-top: 14px; list-style: none; font-size: 12.5px; }
  .contact-list li { display: flex; align-items: center; gap: 8px; line-height: 1.5; }
  .contact-icon { width: 11px; height: 11px; flex: none; }
  /* Back */
  .card-back {
    background: var(--card-black);
    display: flex; flex-direction: column; align-items: center; justify-content: center; gap: 18px;
  }
  .back-square { width: 56px; height: 56px; border: 3px solid var(--soft-grey); }
  .back-name {
    font-weight: 700; font-size: 30px; letter-spacing: 3px;
    text-transform: uppercase; color: var(--soft-grey);
  }
</style>
</head>
<body>
<main class="stage">
  <section class="card card-front" aria-label="Card front">
    <svg class="front-panel" viewBox="0 0 525 300" preserveAspectRatio="none" aria-hidden="true">
      <polygon points="0,120 95,120 200,60 222,250 210,300 0,300" fill="var(--panel-black)"/>
    </svg>
    <div class="front-panel-name">Caldrow Supplies</div>
    <div class="front-content">
      <div class="brand-lockup"><span class="brand-square"></span>Caldrow Supplies</div>
      <h1 class="person-name">Evan Marlow</h1>
      <p class="person-title">President</p>
      <p class="address">412 Larkspur Road<br>Halden, Canada 58210</p>
      <ul class="contact-list">
        <li>
          <svg class="contact-icon" viewBox="0 0 12 12"><path d="M2 1h3l1 3-2 1a6 6 0 0 0 3 3l1-2 3 1v3c-6 1-10-3-9-9z" fill="var(--accent-cyan)"/></svg>
          555-210-4837
        </li>
        <li>
          <svg class="contact-icon" viewBox="0 0 12 12"><rect x="3" y="0.5" width="6" height="11" rx="1" fill="none" stroke="var(--accent-cyan)" stroke-width="1.3"/></svg>
          555-210-6619
        </li>
        <li>
          <svg class="contact-icon" viewBox="0 0 12 12"><rect x="0.5" y="2" width="11" height="8" fill="none" stroke="var(--accent-cyan)" stroke-width="1.3"/><path d="M1 2.5l5 4 5-4" fill="none" stroke="var(--accent-cyan)" stroke-width="1.3"/></svg>
          info@caldrowsupplies.com
        </li>
        <li>
          <svg class="contact-icon" viewBox="0 0 12 12"><circle cx="6" cy="6" r="5.3" fill="none" stroke="var(--accent-cyan)" stroke-width="1.2"/><path d="M1 6h10M6 1c-3 3-3 7 0 10M6 1c3 3 3 7 0 10" fill="none" stroke="var(--accent-cyan)" stroke-width="1"/></svg>
          www.caldrowsupplies.com
        </li>
      </ul>
    </div>
  </section>

  <section class="card card-back" aria-label="Card back">
    <span class="back-square" aria-hidden="true"></span>
    <p class="back-name">Caldrow Supplies</p>
  </section>
</main>
</body>
</html>
```